GHollis Busisness Card

I am an aerospace consultant and at this time only need business cards.

Industry/Entity Type

Business

Contact Information for Business Card

Hollis Partners,LLC
Gerald T. Hollis

348 Birch Hollow Road
Madison AL 35762

256-555-0148 (cell)
256-555-0173 (fax)

geraldhollis@mailbrook.net

```html
<!DOCTYPE html>
<html lang="en">
<head>
<meta charset="utf-8">
<title>Hollis Partners – Business Card</title>
<link rel="stylesheet" href="https://fonts.googleapis.com/css2?family=Open+Sans:wght@400&family=Arimo:wght@400&display=swap">
<style>
  :root {
    --olive: #a0a52c;
    --ink: #5f5f5f;
    --ink-soft: #555555;
    --card-bg: #fdfdfd;
    --card-edge: #e4e4e4;
    --page-bg: #ffffff;
  }
  * { margin: 0; padding: 0; box-sizing: border-box; }
  html, body { width: 1200px; height: 901px; overflow: hidden; background: var(--page-bg); }
  .canvas {
    position: relative; width: 1200px; height: 901px;
    border: 1px solid var(--card-edge); background: var(--page-bg);
  }
  .accent-top { position: absolute; left: 1018px; top: 3px; width: 182px; height: 15px; background: var(--olive); }
  .accent-bottom { position: absolute; left: 0; top: 885px; width: 183px; height: 15px; background: var(--olive); }

  .card {
    position: absolute; left: 111px; top: 155px; width: 980px; height: 594px;
    background: var(--card-bg); border: 2px solid var(--card-edge);
  }
  .card-spine { position: absolute; left: -2px; top: -2px; width: 35px; height: 594px; background: var(--olive); }

  .company {
    position: absolute; left: 96px; top: 42px;
    font-family: "Open Sans", sans-serif; font-weight: 400;
    font-size: 62px; line-height: 1; color: var(--ink); letter-spacing: 1px;
  }

  .holder { position: absolute; left: 58px; top: 376px; }
  .holder-name {
    font-family: "Open Sans", sans-serif; font-size: 43px; line-height: 1;
    color: var(--ink); white-space: nowrap;
  }
  .holder-title {
    margin: 14px 0 0 40px;
    font-family: "Arimo", Arial, sans-serif; font-size: 18px; color: var(--olive);
  }

  .divider { position: absolute; left: 402px; top: 340px; width: 8px; height: 180px; background: var(--olive); }

  .contacts { position: absolute; left: 472px; top: 300px; list-style: none; }
  .contact {
    position: absolute; left: 0; display: flex; align-items: center;
    font-family: "Arimo", Arial, sans-serif; font-size: 30px; color: var(--ink-soft);
    white-space: nowrap;
  }
  .contact svg { width: 30px; height: 30px; fill: var(--olive); margin-right: 30px; flex: none; }
  .contact-phone { top: 2px; }
  .contact-fax { top: 60px; }
  .contact-email { top: 120px; }
  .contact-address { top: 180px; align-items: flex-start; font-family: "Open Sans", sans-serif; font-size: 28px; line-height: 43px; }
  .contact-address svg { margin-top: 6px; }
  .contact-address span { display: block; }
  .contact-address span + span { padding-left: 8px; }
</style>
</head>
<body>
<div class="canvas">
  <div class="accent-top"></div>
  <div class="accent-bottom"></div>

  <section class="card">
    <div class="card-spine"></div>
    <div class="company">Hollis Partners</div>

    <div class="holder">
      <div class="holder-name">Gerald T. Hollis</div>
      <div class="holder-title">Managing Director</div>
    </div>

    <div class="divider"></div>

    <ul class="contacts">
      <li class="contact contact-phone">
        <svg viewBox="0 0 24 24" aria-hidden="true"><path d="M6.6 2.5l2.6 3.8c.4.6.3 1.4-.2 1.9L7.6 9.6c1 2.6 3.2 4.9 5.8 6.1l1.5-1.5c.5-.5 1.3-.6 1.9-.2l3.7 2.6c.6.4.8 1.3.3 1.9l-1.6 2.1c-.6.8-1.7 1.1-2.7.8C9.9 19.3 4.6 14 2.5 7.4c-.3-1 0-2 .8-2.6l2.1-1.7c.4-.4 1-.3 1.2.4z"/><path d="M14 4.5a6 6 0 0 1 5.5 5.5h-1.6A4.5 4.5 0 0 0 14 6.1z"/></svg>
        256-555-0148
      </li>
      <li class="contact contact-fax">
        <svg viewBox="0 0 24 24" aria-hidden="true"><path d="M6 2h12v5H6z"/><path d="M3 8h18a2 2 0 0 1 2 2v7h-4v-3H5v3H1v-7a2 2 0 0 1 2-2z"/><path d="M6 15h12v7H6z"/><rect x="8" y="17" width="8" height="1.4" fill="#fff"/><rect x="8" y="19.4" width="8" height="1.4" fill="#fff"/></svg>
        256-555-0173
      </li>
      <li class="contact contact-email">
        <svg viewBox="0 0 24 24" aria-hidden="true"><path d="M2 5h20v14H2zM3.6 6.6v10.8h16.8V6.6l-8.4 7-8.4-7zm1.6 0l6.8 5.7 6.8-5.7z" fill-rule="evenodd"/></svg>
        geraldhollis@mailbrook.net
      </li>
      <li class="contact contact-address">
        <svg viewBox="0 0 24 24" aria-hidden="true"><path d="M12 1a8 8 0 0 0-8 8c0 5.5 8 14 8 14s8-8.5 8-14a8 8 0 0 0-8-8zm0 4.5a3.5 3.5 0 1 1 0 7 3.5 3.5 0 0 1 0-7z" fill-rule="evenodd"/></svg>
        <div><span>348 Birch Hollow Road Madison,</span><span>AL 35762</span></div>
      </li>
    </ul>
  </section>
</div>
</body>
</html>
```